Brett Olsen Building Business Card Design

Hi,

I need a business card for my Building company.
I am a Builder and build homes for clients.
I am looking for a sophisticated logo that can be used on business cards, envelopes and letter heads.
I am trying to take my business to the next level and need a professional business card.

Colours: Please use white, black, dark grey and bright blue.

Thank you,

Carol and Brett.

Target Market(s)

1. Home and Building Companies 2. Potential customers

Industry/Entity Type

Business

Contact Information for Business Card

Brett Olsen Building PTY LTD

Brett Olsen

Director

A.B.N. 37 829 516 073

BUILDERS LICENCE No. 573019k

Mobile: 0412 907 381

Email: brettolsenbuilding@mailvane.com.au

Requirements
Must have
• The following is compulsory to have in the designs:

Brett Olsen Building PTY LTD (business name)

Brett Olsen (contact name)

Director (position)

A.B.N. 37 829 516 073

Builders Licence No. 573019k

Mobile: 0412 907 381

Nice to have
• Logo for business
Should not have
• Should not be cluttered.

I am looking for a clean, sophisticated and professional business card design.

```html
<!DOCTYPE html>
<html lang="en">
<head>
<meta charset="utf-8">
<title>Brett Olsen Building – Business Card</title>
<link href="https://fonts.googleapis.com/css2?family=Source+Sans+3:wght@400;700&display=swap" rel="stylesheet">
<style>
  :root {
    --page-grey: #dadada;
    --label-ink: #333333;
    --card-white: #ffffff;
    --brand-blue: #0a80cf;
    --ink-dark: #3a3a3a;
    --ink-white: #ffffff;
  }
  * { margin: 0; padding: 0; box-sizing: border-box; }
  html, body {
    width: 958px;
    height: 1200px;
    overflow: hidden;
    background: var(--page-grey);
    font-family: "Source Sans 3", "Myriad Pro", sans-serif;
  }
  .sheet { position: relative; width: 958px; height: 1200px; }

  .side-label {
    position: absolute;
    left: 115px;
    font-family: Arial, Helvetica, sans-serif;
    font-size: 18px;
    color: var(--label-ink);
  }
  .side-label--front { top: 66px; }
  .side-label--back { top: 620px; }

  .card {
    position: absolute;
    left: 95px;
    width: 769px;
    height: 447px;
    overflow: hidden;
  }
  .card--front { top: 104px; background: var(--card-white); }
  .card--back { top: 657px; background: var(--brand-blue); color: var(--ink-white); }

  .corner-tab {
    position: absolute;
    right: 0;
    top: 0;
    width: 37px;
    height: 38px;
    background: var(--brand-blue);
  }

  .brand {
    position: absolute;
    left: 83px;
    top: 66px;
    display: flex;
    align-items: center;
    gap: 22px;
  }
  .brand__mark {
    width: 96px;
    height: 96px;
    background: var(--brand-blue);
  }
  .brand__name {
    font-size: 34px;
    line-height: 32px;
    font-weight: 400;
    letter-spacing: 1px;
    text-transform: uppercase;
    color: var(--ink-dark);
  }

  .registration {
    position: absolute;
    left: 84px;
    top: 288px;
    font-size: 29px;
    line-height: 44px;
    color: var(--ink-dark);
  }
  .registration b { font-weight: 700; }

  .swoosh {
    position: absolute;
    left: 0;
    bottom: 0;
    width: 769px;
    height: 447px;
  }

  .contact-name {
    position: absolute;
    left: 51px;
    top: 116px;
  }
  .contact-name__person {
    font-size: 41px;
    line-height: 44px;
    font-weight: 700;
  }
  .contact-name__role {
    font-size: 33px;
    line-height: 40px;
    font-weight: 400;
  }

  .contact-lines {
    position: absolute;
    left: 51px;
    top: 352px;
    font-size: 24px;
    line-height: 34px;
  }
  .contact-lines b { font-weight: 700; }
</style>
</head>
<body>
<main class="sheet">
  <p class="side-label side-label--front">Front</p>
  <section class="card card--front">
    <div class="corner-tab"></div>
    <div class="brand">
      <div class="brand__mark"></div>
      <p class="brand__name">Brett<br>Olsen<br>Building</p>
    </div>
    <p class="registration">
      <b>A.B.N.</b> 37 829 516 073<br>
      <b>Builders Licence No.</b> 573019k
    </p>
    <svg class="swoosh" viewBox="0 0 769 447" aria-hidden="true">
      <path d="M0 359 C 90 415 220 440 431 447 L0 447 Z" fill="var(--brand-blue)"/>
    </svg>
  </section>

  <p class="side-label side-label--back">Back</p>
  <section class="card card--back">
    <div class="contact-name">
      <p class="contact-name__person">Brett Olsen</p>
      <p class="contact-name__role">Director</p>
    </div>
    <p class="contact-lines">
      <b>Mobile:</b> 0412 907 381<br>
      <b>Email:</b> brettolsenbuilding@mailvane.com.au
    </p>
  </section>
</main>
</body>
</html>
```